Velo Crest Business Card

Need a professional but with a touch of unique looking Business Card for my staff.

Target Market(s)

Corporate

Industry/Entity Type

Business

Requirements
Must have
• 40mm height

```html
<!DOCTYPE html>
<html lang="en">
<head>
<meta charset="utf-8">
<title>Velo Crest Business Card</title>
<link rel="stylesheet" href="https://fonts.googleapis.com/css2?family=Arimo:ital,wght@0,400;0,700;1,700&display=swap">
<style>
  :root {
    --stage: #5a5a5a;
    --ink: #000000;
    --panel: #0b0b0b;
    --paper: #ffffff;
    --soft: #d9d9d9;
    --muted: #e6e6e6;
  }
  * { margin: 0; padding: 0; box-sizing: border-box; }
  html, body { width: 1200px; height: 534px; overflow: hidden; }
  body {
    background: var(--stage);
    font-family: "Arimo", Arial, sans-serif;
    position: relative;
  }
  .card {
    position: absolute;
    top: 119px;
    width: 517px;
    height: 295px;
    background: var(--paper);
    overflow: hidden;
  }
  .card--front { left: 62px; }
  .card--back { left: 622px; }

  .front-panel {
    position: absolute; left: 0; top: 0;
    width: 100%; height: 269px;
    background: radial-gradient(ellipse at 30% 40%, #1a1a1a 0%, var(--panel) 70%);
  }
  .wordmark {
    color: var(--paper);
    font-weight: 400;
    letter-spacing: -1px;
    line-height: 1;
  }
  .front-panel .wordmark {
    position: absolute; left: 0; right: 0; top: 84px;
    text-align: center;
    font-size: 92px;
  }
  .front-url {
    position: absolute; left: 0; right: 0; top: 214px;
    text-align: center;
    color: var(--paper);
    font-size: 18px;
    letter-spacing: 1.5px;
  }

  .back-head {
    position: absolute; left: 0; top: 0;
    width: 100%; height: 113px;
    background: var(--paper);
  }
  .back-head .wordmark {
    position: absolute; left: 46px; top: 30px;
    color: var(--ink);
    font-size: 60px;
  }
  .wave-field {
    position: absolute; right: 0; top: 0;
    width: 200px; height: 113px;
    background: linear-gradient(100deg, var(--paper) 0%, var(--muted) 60%, var(--paper) 100%);
  }
  .back-panel {
    position: absolute; left: 0; top: 113px;
    width: 100%; height: 157px;
    background: var(--panel);
  }
  .notch { position: absolute; left: 54px; }
  .notch--top { top: 113px; }
  .notch--bottom { top: 254px; }

  .company {
    position: absolute; left: 56px; top: 34px;
    color: var(--paper);
  }
  .company-name { font-size: 16px; font-weight: 700; font-style: italic; }
  .company-tagline { font-size: 12px; margin-top: 3px; }
  .company-address { font-size: 13px; line-height: 22px; margin-top: 11px; }

  .contacts {
    position: absolute; left: 294px; top: 34px;
    list-style: none;
    color: var(--paper);
    font-size: 14px;
  }
  .contacts li { display: flex; align-items: center; height: 22.5px; }
  .contacts svg { width: 14px; height: 14px; margin-right: 9px; flex: none; }
</style>
</head>
<body>
  <section class="card card--front">
    <div class="front-panel" role="img" aria-label="Dark panel with a subtle square grid texture">
      <div class="wordmark">velocrest</div>
      <div class="front-url">www.velocrest.edu.au</div>
    </div>
  </section>

  <section class="card card--back">
    <div class="back-head">
      <div class="wave-field" role="img" aria-label="Fine grey flowing line texture"></div>
      <div class="wordmark">velocrest</div>
    </div>
    <div class="back-panel">
      <div class="company">
        <div class="company-name">Velo Crest</div>
        <div class="company-tagline">IT Training &amp; Certifications</div>
        <div class="company-address">Level One / 180 Arden Lane<br>Melbourne, 3004</div>
      </div>
      <ul class="contacts">
        <li>
          <svg viewBox="0 0 14 14"><path d="M4 1 L6 4 L4.5 5.5 Q6 9 8.5 9.5 L10 8 L13 10 L11.5 13 Q3 12 1 3 Z" fill="none" stroke="#fff" stroke-width="1.2"/></svg>
          (03) 9000 1234
        </li>
        <li>
          <svg viewBox="0 0 14 14"><rect x="3" y="1.5" width="8" height="5" fill="none" stroke="#fff" stroke-width="1.2"/><rect x="1" y="7" width="12" height="5.5" fill="#fff"/></svg>
          (03) 9000 5678
        </li>
        <li>
          <svg viewBox="0 0 14 14"><rect x="1" y="3" width="12" height="8" fill="none" stroke="#fff" stroke-width="1.2"/><path d="M1 3 L7 8 L13 3" fill="none" stroke="#fff" stroke-width="1.2"/></svg>
          info@velocrest.edu.au
        </li>
        <li>
          <svg viewBox="0 0 14 14"><circle cx="7" cy="7" r="5.6" fill="none" stroke="#fff" stroke-width="1.1"/><ellipse cx="7" cy="7" rx="2.4" ry="5.6" fill="none" stroke="#fff" stroke-width="1"/><path d="M1.4 7 H12.6" stroke="#fff" stroke-width="1"/></svg>
          www.velocrest.edu.au
        </li>
      </ul>
    </div>
    <svg class="notch notch--top" width="24" height="14" viewBox="0 0 24 14"><path d="M0 0 H24 L12 13 Z" fill="#ffffff"/></svg>
    <svg class="notch notch--bottom" width="24" height="16" viewBox="0 0 24 16"><path d="M0 16 H24 L12 1 Z" fill="#ffffff"/></svg>
  </section>
</body>
</html>
```